Fashion Design Business Card

I need a new business card designed for a new fashion company. I have attached what I have currently designed. I want it more feminine looking, the logo needs to be gold. I want it simple, feminine and stylish. Please give me some different ideas with the fonts.

I need to send the design we currently have, as we have worked out the logo.
You also need all of our details
Fashion

```html
<!DOCTYPE html>
<html lang="en">
<head>
<meta charset="utf-8">
<title>Marlena Hart — Business Card</title>
<link rel="stylesheet" href="https://fonts.googleapis.com/css2?family=Libre+Baskerville:wght@400;700&display=swap">
<style>
  :root {
    --backdrop: #e9e4dd;
    --card-brown: #3e3530;
    --card-white: #ffffff;
    --ink: #1d1a18;
    --mark-grey: #c4c2c0;
    --gold: #e8b514;
    --back-centre: #4a3f38;
    --back-edge: #141110;
    --url-grey: #6d6661;
  }
  * { margin: 0; padding: 0; box-sizing: border-box; }
  html, body {
    width: 1200px; height: 900px; overflow: hidden;
    background: var(--backdrop);
    font-family: "Libre Baskerville", "Times New Roman", serif;
  }
  .stage { position: relative; width: 1200px; height: 900px; }
  .card {
    position: absolute; left: 265px; width: 670px; height: 380px;
    overflow: hidden;
    box-shadow: 0 6px 16px rgba(0,0,0,0.35);
  }
  /* Front */
  .card--front { top: 50px; background: var(--card-brown); }
  .front-band {
    position: absolute; left: 0; top: 80px; width: 100%; height: 222px;
    background: var(--card-white); overflow: hidden;
  }
  .front-brand {
    position: absolute; left: 20px; top: 0; width: 300px; height: 222px;
    display: flex; align-items: center; justify-content: center;
    color: var(--mark-grey); font-weight: 700; font-size: 26px; letter-spacing: 2px;
    white-space: nowrap;
  }
  .front-details {
    position: absolute; left: 366px; top: 36px; color: var(--ink);
  }
  .holder-name {
    font-weight: 700; font-size: 25px; letter-spacing: 2px; line-height: 1;
  }
  .holder-role { font-size: 19px; margin-top: 6px; color: #2b2725; }
  .contact-list { margin-top: 14px; }
  .contact-line { font-size: 15px; line-height: 22px; }
  .contact-web { font-size: 15px; margin-top: 16px; }

  /* Back */
  .card--back {
    top: 470px;
    background: radial-gradient(ellipse 60% 70% at 50% 22%, var(--back-centre) 0%, #2a2421 55%, var(--back-edge) 100%);
    text-align: center;
  }
  .back-dot {
    position: absolute; left: 50%; top: 150px; width: 28px; height: 28px;
    margin-left: -14px; background: var(--gold);
  }
  .back-name {
    position: absolute; left: 0; right: 0; top: 246px;
    color: var(--gold); font-weight: 700; font-size: 27px; letter-spacing: 2px;
  }
  .back-web {
    position: absolute; left: 0; right: 0; top: 340px;
    color: var(--url-grey); font-size: 12px; letter-spacing: 4px;
  }
</style>
</head>
<body>
<main class="stage">
  <section class="card card--front" aria-label="Card front">
    <div class="front-band">
      <div class="front-brand">MARLENA HART</div>
      <div class="front-details">
        <h1 class="holder-name">MARLENA HART</h1>
        <p class="holder-role">fashion designer</p>
        <div class="contact-list">
          <p class="contact-line">P : 0400123456</p>
          <p class="contact-line">e : marlena@marlenahart.com</p>
        </div>
        <p class="contact-web">www.marlenahart.com</p>
      </div>
    </div>
  </section>

  <section class="card card--back" aria-label="Card back">
    <div class="back-dot" aria-hidden="true"></div>
    <p class="back-name">MARLENA HART</p>
    <p class="back-web">www.marlenahart.com</p>
  </section>
</main>
</body>
</html>
```